Shopify website design for clothing brand.

We need a website design for our clothing brand. We are looking for a colourful and fun design to fit into the brand concept.

```html
<!DOCTYPE html>
<html lang="en">
<head>
<meta charset="utf-8">
<title>Wrenloom — Clothing</title>
<link rel="stylesheet" href="https://fonts.googleapis.com/css2?family=Comfortaa:wght@600;700&family=Nunito+Sans:wght@400;600;700&display=swap">
<style>
:root{
  --plum:#6f1550;
  --yellow:#fff200;
  --cream:#fff8c2;
  --lilac:#e4d0dd;
  --ink:#1f1f1f;
  --muted:#555;
  --card:#f5f5f5;
  --footer:#262626;
  --white:#fff;
}
*{box-sizing:border-box;margin:0;padding:0}
html,body{width:1200px;height:3531px;overflow:hidden}
body{position:relative;font-family:"Nunito Sans",sans-serif;color:var(--ink);background:var(--white)}
.abs{position:absolute}
.display{font-family:"Comfortaa",sans-serif;font-weight:700}
.announce{left:0;top:0;width:1200px;height:34px;background:var(--plum);color:var(--white);font-size:13px;display:flex;align-items:center;justify-content:center}
.brand{font-family:"Nunito Sans",sans-serif;font-weight:700;color:#f5c400;letter-spacing:1px;display:flex;align-items:center;gap:10px}
.brand .dot{width:12px;height:12px;border-radius:50%;background:var(--plum)}
.header-brand{left:206px;top:66px;font-size:34px}
.search{left:481px;top:64px;width:438px;height:43px;border:1px solid #cfcfcf;border-radius:22px}
.search svg{position:absolute;right:22px;top:13px}
.icon-btn{top:75px}
.nav{top:131px;font-size:16px;display:flex}
.nav a{position:absolute;color:var(--ink);text-decoration:none;white-space:nowrap}
.nav .active::after{content:"";position:absolute;left:-1px;right:-1px;top:28px;height:2px;background:var(--ink)}
.hero{left:0;top:165px;width:1200px;height:470px;background:linear-gradient(180deg,#b88a6e 0%,#a4594f 45%,#8e2f52 100%)}
.hero h1{position:absolute;left:0;width:1200px;top:280px;text-align:center;color:var(--white);font-size:52px}
.btn{display:flex;align-items:center;justify-content:center;gap:10px;border-radius:24px;font-size:16px;font-weight:600;position:absolute}
.btn-yellow{background:var(--yellow);color:var(--ink)}
.btn-plum{background:var(--plum);color:var(--white)}
.feature{top:665px;height:176px;width:386px;display:flex;flex-direction:column;align-items:center;justify-content:center;gap:8px;font-size:16px}
.section-title{left:0;width:1200px;text-align:center;font-size:44px}
.collection{top:985px;width:288px;height:388px}
.collection span{position:absolute;left:33px;bottom:33px;color:var(--white);font-weight:600;font-size:16px;display:flex;gap:10px;align-items:center}
.product{width:224px}
.product .thumb{height:244px;background:var(--card);border-radius:10px;position:relative;display:flex;align-items:center;justify-content:center}
.product .photo{width:130px;height:160px;border-radius:18px}
.badge{position:absolute;right:14px;top:12px;background:var(--plum);color:var(--white);font-size:11px;padding:2px 9px;border-radius:10px}
.product h3{font-weight:400;font-size:18px;text-align:center;margin-top:22px;letter-spacing:.3px}
.product p{font-size:14px;color:var(--muted);text-align:center;margin-top:8px}
.product .price{font-size:14px;color:var(--ink);margin-top:10px}
.divider{left:112px;top:2097px;width:977px;height:1px;background:#e2e2e2}
.promo{top:2730px;height:318px;width:587px}
.promo h2{position:absolute;left:0;right:0;top:165px;text-align:center;color:var(--white);font-size:34px}
.footer{left:0;top:3096px;width:1200px;height:435px;background:var(--footer);color:#e8e8e8}
.footer .brand{position:absolute;left:112px;top:80px;font-size:32px}
.footer p.about{position:absolute;left:112px;top:132px;width:400px;font-size:15px;line-height:28px}
.footer h4{font-size:16px;font-weight:700;color:var(--white)}
.footer .col{position:absolute;top:74px}
.footer ul{list-style:none;margin-top:26px}
.footer li{font-size:15px;height:34px;display:flex;align-items:center;gap:9px}
.footer .info{position:absolute;font-size:15px;line-height:28px}
.social-dot{width:8px;height:8px;border-radius:50%;background:#e8e8e8}
.payments{position:absolute;left:403px;top:362px;display:flex;gap:4px}
.payments i{display:block;width:32px;height:20px;border-radius:3px;background:#d9d9d9}
.payments i:nth-child(3n+1){background:#3b6cc4}
.payments i:nth-child(4n+2){background:#f0f0f0}
.copyright{position:absolute;left:0;width:1200px;top:402px;text-align:center;font-size:13px;color:#bdbdbd}
</style>
</head>
<body>

<div class="abs announce">Seasonal sale! Save 10% on all sweaters. Free shipping for all orders over $$$.</div>

<header>
  <div class="abs brand header-brand"><span class="dot"></span>WRENLOOM</div>
  <div class="abs search">
    <svg width="17" height="17" viewBox="0 0 24 24" fill="none" stroke="#333" stroke-width="2"><circle cx="10" cy="10" r="7"/><path d="M15 15l6 6"/></svg>
  </div>
  <svg class="abs icon-btn" style="left:934px" width="20" height="22" viewBox="0 0 24 24" fill="none" stroke="#333" stroke-width="1.8"><circle cx="12" cy="8" r="4.5"/><path d="M3.5 22c0-5 4-8 8.5-8s8.5 3 8.5 8z"/></svg>
  <svg class="abs icon-btn" style="left:973px" width="22" height="22" viewBox="0 0 24 24" fill="none" stroke="#333" stroke-width="1.8"><path d="M2 3h3l2.5 12h12L22 7H6"/><circle cx="9" cy="20" r="1.5"/><circle cx="18" cy="20" r="1.5"/></svg>
  <nav class="abs nav" style="left:0;width:1200px">
    <a class="active" style="left:443px">Home</a>
    <a style="left:520px">Shop &#8964;</a>
    <a style="left:603px">News</a>
    <a style="left:676px">Contact Us</a>
  </nav>
</header>

<section class="abs hero" role="img" aria-label="Woman in a red outfit seated on a wicker chair beside a potted plant">
  <h1 class="display">So many ways to express yourself</h1>
  <a class="btn btn-yellow" style="left:529px;top:360px;width:142px;height:46px">Shop Now <span>&#8594;</span></a>
</section>

<section>
  <div class="abs feature" style="left:0;background:var(--cream)">
    <svg width="28" height="32" viewBox="0 0 24 28" fill="none" stroke="#111" stroke-width="2"><path d="M12 22s-7-7-7-12a7 7 0 0114 0c0 5-7 12-7 12z"/><circle cx="12" cy="10" r="2.5"/><path d="M4 25h16"/></svg>
    Locally Owned
  </div>
  <div class="abs feature" style="left:407px;background:var(--lilac)">
    <svg width="50" height="32" viewBox="0 0 40 26" fill="#111"><rect x="6" y="3" width="20" height="15" rx="1"/><path d="M26 8h7l5 6v4H26z"/><circle cx="12" cy="21" r="3.5"/><circle cx="31" cy="21" r="3.5"/><rect x="0" y="7" width="5" height="2"/><rect x="1" y="12" width="4" height="2"/></svg>
    Fast Shipping
  </div>
  <div class="abs feature" style="left:815px;background:var(--cream)">
    <svg width="30" height="34" viewBox="0 0 24 28" fill="none" stroke="#111" stroke-width="2"><circle cx="12" cy="10" r="7"/><path d="M9 10l2 2 4-4"/><path d="M7 16l-3 8 4-1 2 3 2-6M17 16l3 8-4-1-2 3-2-6"/></svg>
    365 Day Guarantee
  </div>
</section>

<section>
  <h2 class="abs display section-title" style="top:900px">Collection list</h2>
  <div class="abs collection" style="left:0;background:linear-gradient(180deg,#4d5b3e,#c8bcb0)" role="img" aria-label="Woman in sunglasses and pale tee against green foliage"><span>Graphic Tees &#8594;</span></div>
  <div class="abs collection" style="left:304px;background:linear-gradient(180deg,#8a8a88,#2f5a55)" role="img" aria-label="Man in a teal hoodie on a grey backdrop"><span>Men's &#8594;</span></div>
  <div class="abs collection" style="left:609px;background:linear-gradient(180deg,#2f6a82,#b95a2e)" role="img" aria-label="Woman in an orange jacket under a blue sky"><span>Women's &#8594;</span></div>
  <div class="abs collection" style="left:913px;background:linear-gradient(180deg,#b7a48c,#4a4440)" role="img" aria-label="Man in a checked blazer sitting on stone steps"><span>Apparel &#8594;</span></div>
  <a class="btn btn-plum" style="left:514px;top:1412px;width:172px;height:46px">All Collection <span>&#8594;</span></a>
</section>

<section>
  <h2 class="abs display section-title" style="top:1526px">Our Featured</h2>
  <div class="abs product" style="left:112px;top:1611px"><div class="thumb"><span class="badge">On Sale</span><div class="photo" style="background:#6d6d45" role="img" aria-label="Olive hoodie"></div></div><h3>Lorem ipsum</h3><p>Neque porro quisquam est</p><p class="price">$8.99</p></div>
  <div class="abs product" style="left:362px;top:1611px"><div class="thumb"><div class="photo" style="background:#222;height:90px" role="img" aria-label="Black trucker cap"></div></div><h3>Lorem ipsum</h3><p>Neque porro quisquam est</p><p class="price">$8.99</p></div>
  <div class="abs product" style="left:614px;top:1611px"><div class="thumb"><div class="photo" style="background:#9c9c9c" role="img" aria-label="Grey t-shirt"></div></div><h3>Lorem ipsum</h3><p>Neque porro quisquam est</p><p class="price">$8.99</p></div>
  <div class="abs product" style="left:865px;top:1611px"><div class="thumb"><div class="photo" style="background:#111" role="img" aria-label="Black t-shirt"></div></div><h3>Lorem ipsum</h3><p>Neque porro quisquam est</p><p class="price">$8.99</p></div>
  <a class="btn btn-yellow" style="left:485px;top:1998px;width:229px;height:46px">Shop this collection <span>&#8594;</span></a>
</section>

<div class="abs divider"></div>

<section>
  <h2 class="abs display section-title" style="top:2144px">Apparel</h2>
  <div class="abs product" style="left:112px;top:2228px"><div class="thumb"><span class="badge">On Sale</span><div class="photo" style="background:#f1aaa6" role="img" aria-label="Pink hoodie"></div></div><h3>Lorem ipsum</h3><p>Neque porro quisquam est</p><p class="price">$8.99</p></div>
  <div class="abs product" style="left:362px;top:2228px"><div class="thumb"><div class="photo" style="background:#e2e2e2;height:90px" role="img" aria-label="White bucket hat"></div></div><h3>Lorem ipsum</h3><p>Neque porro quisquam est</p><p class="price">$8.99</p></div>
  <div class="abs product" style="left:614px;top:2228px"><div class="thumb"><span class="badge">On Sale</span><div class="photo" style="background:#9c9c9c" role="img" aria-label="Grey t-shirt"></div></div><h3>Lorem ipsum</h3><p>Neque porro quisquam est</p><p class="price">$8.99</p></div>
  <div class="abs product" style="left:865px;top:2228px"><div class="thumb"><div class="photo" style="background:#d4d98a" role="img" aria-label="Lime sweatshirt"></div></div><h3>Lorem ipsum</h3><p>Neque porro quisquam est</p><p class="price">$8.99</p></div>
  <a class="btn btn-plum" style="left:485px;top:2615px;width:229px;height:46px">Shop this collection <span>&#8594;</span></a>
</section>

<section>
  <div class="abs promo" style="left:0;background:linear-gradient(135deg,#b9b8b2,#d9732b 60%,#e9e4dc)" role="img" aria-label="Woman in an orange hooded jacket and tinted glasses">
    <h2 class="display">Planet-friendly garments</h2>
    <a class="btn btn-yellow" style="left:223px;top:225px;width:142px;height:45px">Shop Now <span>&#8594;</span></a>
  </div>
  <div class="abs promo" style="left:613px;background:linear-gradient(135deg,#d7d4d0,#b98259 55%,#cfcac4)" role="img" aria-label="Woman in a knit sweater and tan trousers seated on the floor">
    <h2 class="display">Our clothes are made to last</h2>
    <a class="btn btn-yellow" style="left:222px;top:225px;width:142px;height:45px">Shop Now <span>&#8594;</span></a>
  </div>
</section>

<footer class="abs footer">
  <div class="brand"><span class="dot"></span>WRENLOOM</div>
  <p class="about">Lorem ipsum dolor sit amet, consectetur adipiscing elit, sed do eiusmod tempor incididunt ut labore et dolore magna aliqua. facilisis.</p>
  <div class="info" style="left:112px;top:226px"><h4>Address</h4>Wrenloom,<br>Address comes here.</div>
  <div class="info" style="left:309px;top:226px"><h4>Phone</h4>+1 555-010-0199<h4>Email</h4>info@wrenloom.com</div>
  <div class="col" style="left:566px"><h4>Shop Wrenloom</h4><ul><li>Search</li><li>Shop All</li><li>About Us</li><li>Contact Us</li></ul></div>
  <div class="col" style="left:764px"><h4>Customer Services</h4><ul><li>Contact Us</li><li>Terms &amp; Conditions</li><li>Privacy Policy</li></ul></div>
  <div class="col" style="left:952px"><h4>Follow Us</h4><ul><li><span class="social-dot"></span>Facetome</li><li><span class="social-dot"></span>Chatter</li><li><span class="social-dot"></span>Pinwall</li><li><span class="social-dot"></span>Snapgram</li></ul></div>
  <div class="payments" aria-label="Accepted payment methods"><i></i><i></i><i></i><i></i><i></i><i></i><i></i><i></i><i></i><i></i><i></i></div>
  <div class="copyright">2023 Wrenloom. All Rights Reserved.</div>
</footer>

</body>
</html>
```